Covid 19 Exit Strategy one page brochure

I would like to design, and will need URGENT help, a brochure detailing a Covid 19 Exit Strategy plan. This brochure will need to be understood easily and the graphics inside should make it easy for people to understand without reading the entire text. This project is quite urgent and needs to be completed THIS WEEK - by Saturday may 16th at the latest. I am attaching two examples. I will provide the text.

```html
<!DOCTYPE html>
<html lang="en">
<head>
<meta charset="utf-8">
<title>Covid-19 Phased Exit Strategy</title>
<link rel="stylesheet" href="https://fonts.googleapis.com/css2?family=Montserrat:wght@400;500;600;700;800&display=swap">
<style>
  :root {
    --backdrop: #d9d9d9;
    --paper: #ffffff;
    --navy: #1d3160;
    --navy-mid: #34548f;
    --navy-light: #5f83bd;
    --red: #d32a2f;
    --ink: #2b2b2b;
    --rule: #b8b8b8;
    --icon-blue: #cfe0f3;
    --icon-red: #f3d2d3;
  }
  * { box-sizing: border-box; margin: 0; padding: 0; }
  html, body { width: 1200px; height: 960px; overflow: hidden; }
  body {
    background: var(--backdrop);
    font-family: "Montserrat", Arial, sans-serif;
    color: var(--ink);
  }
  .flyer {
    position: absolute;
    left: 250px; top: 24px;
    width: 700px; height: 912px;
    background: var(--paper);
    box-shadow: 0 6px 24px rgba(0,0,0,.18);
    overflow: hidden;
    display: flex; flex-direction: column;
    padding-bottom: 26px;
  }
  .hero {
    position: relative;
    flex: none;
    height: 168px;
    display: flex; flex-direction: column; align-items: center; justify-content: flex-end;
    padding-bottom: 18px;
    text-align: center;
  }
  .hero-art {
    position: absolute; inset: 0;
    background: radial-gradient(circle at 20% 60%, var(--navy-light), transparent 45%),
                radial-gradient(circle at 85% 30%, var(--navy-mid), transparent 50%),
                linear-gradient(120deg, var(--navy) 0%, #2a4477 55%, var(--navy) 100%);
  }
  .hero > *:not(.hero-art) { position: relative; }
  .hero-kicker { color: #fff; font-weight: 800; font-size: 27px; letter-spacing: 1px; line-height: 1.1; }
  .hero-title { color: var(--red); font-weight: 800; font-size: 31px; line-height: 1.1; letter-spacing: .5px; }
  .hero-byline { color: #fff; font-weight: 500; font-size: 22px; margin-top: 2px; }

  .intro {
    flex: none;
    padding: 12px 48px 0;
    font-size: 10.4px; line-height: 1.35; text-align: justify;
  }

  .requirements {
    position: relative;
    flex: 1;
    min-height: 0;
    margin: 26px 48px 16px;
    display: grid;
    grid-template-columns: repeat(3, 1fr);
    grid-template-rows: auto auto 1fr;
    border: 1px solid var(--rule);
  }
  .requirements-label {
    position: absolute; top: -13px; left: 50%; transform: translateX(-50%);
    background: var(--red); color: #fff;
    font-weight: 700; font-size: 12px; letter-spacing: .6px;
    padding: 5px 14px; white-space: nowrap;
  }
  .req {
    border-right: 1px solid var(--rule);
    border-bottom: 1px solid var(--rule);
    padding: 20px 14px 10px;
    display: flex; flex-direction: column; align-items: center;
    text-align: justify; text-align-last: center;
    font-size: 10.2px; line-height: 1.3;
  }
  .req:nth-child(3n+1) { border-right: 0; }
  .req:nth-last-child(-n+3) { border-bottom: 0; padding-top: 16px; }
  .req-icon {
    width: 54px; height: 46px; border-radius: 8px; flex: none;
    background: linear-gradient(135deg, var(--icon-blue) 60%, var(--icon-red));
    margin-bottom: 9px;
  }

  .footer-band {
    flex: none;
    height: 52px;
    background: var(--red);
    display: flex; align-items: center; justify-content: center; gap: 18px;
    color: #fff; font-weight: 600; font-size: 20px; letter-spacing: .3px;
  }
</style>
</head>
<body>
  <main class="flyer">
    <header class="hero">
      <div class="hero-art" role="img" aria-label="Close-up background of blue coronavirus particles"></div>
      <p class="hero-kicker">COVID-19</p>
      <h1 class="hero-title">PHASED EXIT STRATEGY</h1>
      <p class="hero-byline">Developed by Dana Ellery</p>
    </header>

    <p class="intro">Pandemics have, historically, seen their end both medically - via herd immunity or immunizations. And while there are several clinical trials underway for potential Covid-19 vaccines, we are still a long way from deploying an effective vaccine and one that will stand the test of time as the virus changes. Covid-19 pandemic will be considered 'ended' when there are only occasional traces of localized cases that are quickly contained in specific locations. Today and in the absence of an effective vaccine(s) and for the re-opening of the economies and social activities to be successful, it is critical that the following basic conditions be in place before any lockdowns are lifted and before social activities resume:</p>

    <section class="requirements">
      <h2 class="requirements-label">GENERAL REQUIREMENTS</h2>
      <div class="req"><div class="req-icon" role="img" aria-label="Document with magnifier showing a downward trend"></div><p>Single digit downward trend of documented cases within the past 14- days.</p></div>
      <div class="req"><div class="req-icon" role="img" aria-label="ICU hospital bed with drip"></div><p>Ability to surge ICU capacity on a short notice - 24h.</p></div>
      <div class="req"><div class="req-icon" role="img" aria-label="Thermometer"></div><p>Mandatory daily checks of body temperature for everyone at the workplace or entering public areas.</p></div>
      <div class="req"><div class="req-icon" role="img" aria-label="Hospital building"></div><p>Hospitals and the health care system are capable of treating patients without operating on a crisis mode.</p></div>
      <div class="req"><div class="req-icon" role="img" aria-label="Globe with arrows between regions"></div><p>Plan in place to trigger targeted or full-scale containment in case of sudden outbreaks</p></div>
      <div class="req"><div class="req-icon" role="img" aria-label="Hand with sanitizer bottle"></div><p>Mandatory sanitation in all places - use of disinfection available on a large scale.</p></div>
      <div class="req"><div class="req-icon" role="img" aria-label="Test tube with blood drop"></div><p>Ability to screen &amp; test symptomatic individuals within 24 hours of identi-fication. Increased and sufficient testing capacity, to test at least 50% of all population if necessary within a timeframe of 3 months.</p></div>
      <div class="req"><div class="req-icon" role="img" aria-label="Patient with monitor and virus symbol"></div><p>Ability to track and traceinfected patients and contacts on a live basis and across the country and ability to react quickly to any unusual trends or outbreaks.</p></div>
      <div class="req"><div class="req-icon" role="img" aria-label="Face mask"></div><p>Mandatory use of masks (at least surgical grade) for everyone in all public areas and at work. Mandatory use of N95, or equivalent, masks for all healthcare front workers and for all government agencies and authorities that are involved in overseeing the containment activities.</p></div>
    </section>

    <footer class="footer-band">
      <span>DON'T HAVE TO GO OUTSIDE ?</span>
      <span>PLEASE STAY AT HOME!</span>
    </footer>
  </main>
</body>
</html>
```